BRISLEY Homes business card Coral Press

I've been a Real Estate agent since 1988. I left the BIG brokerages 2 years ago and am on my own and need a business card. I love doing graphics, but don't have the bandwidth right now.

Background. I want a card that stands out like I do. I'm the fun guy that always has a joke or funny story, and my clients like me. Something fun, but not too silly.

I don't have a symbol or logo that I'm using on the card now, but need to include something, a Font by itself or a logo? I'm not sure if we need a logo or not. I'm open.
The GREAT design is going to be the basis for the next project of stationary, note pads, and Real Estate FOR SALE & Open House signs.

Single sided card is fine, but I selected a 2 sided just in case that's what it works out to be.

Here we go. If you need anything else. Please let me know. As I think of anything, I'll add that also.

Target Market(s)

My territory is Santa Clara County / Silicon Valley, CA. I tend to work with new buyers buying a condo ($500,000) up to single family home for about $1.5 million. 1st time buyers and also move-up buyers. I haven't worked with multi-million $$ homes .... but wouldn't turn it down. Clients here tend to be White, Latin and now many more Chinese and East Indians. Clients also tend to be high tech, Zentrix, Quill, Mingleverse workers and also non tech people.

Industry/Entity Type

Business

Contact Information for Business Card

CONTENT:
Company: BRISLEY Homes
My name: Harold P. Brisley Jr.
Title: Real Estate Broker
Email: Hal@HaroldBrisley.example
Website: www.HaroldBrisley.example
Phone: (408) 555-0172
BRE # 07390418

Font styles to use
Sans Serif

Requirements
Must have
• Content from above. Something that stands out from the others. Serious enough looking, not stale, maybe a bit fun.

```html
<!DOCTYPE html>
<html lang="en">
<head>
<meta charset="utf-8">
<title>BRISLEY Homes – Business Card</title>
<link rel="stylesheet" href="https://fonts.googleapis.com/css2?family=Source+Sans+3:wght@400;600&display=swap">
<style>
  :root {
    --page-bg: #3a3330;
    --card-bg: #1d1d1e;
    --card-bg-edge: #141415;
    --teal: #2a9a8c;
    --text-light: #f2f2f2;
    --divider: #3b3b3d;
  }
  * { margin: 0; padding: 0; box-sizing: border-box; }
  html, body {
    width: 1200px;
    height: 844px;
    overflow: hidden;
    background: var(--page-bg);
    font-family: "Source Sans 3", sans-serif;
  }
  .card-set {
    position: relative;
    width: 1200px;
    height: 844px;
  }
  .card {
    position: absolute;
    top: 276px;
    width: 510px;
    height: 292px;
    background: radial-gradient(ellipse at 40% 30%, var(--card-bg) 0%, var(--card-bg-edge) 100%);
    border-radius: 3px;
    box-shadow: 0 10px 28px rgba(0,0,0,.45);
  }
  .card--front { left: 55px; }
  .card--back  { left: 635px; }

  .brand {
    position: absolute;
    left: 0; right: 0;
    text-align: center;
    color: var(--teal);
    font-weight: 400;
    letter-spacing: 3px;
    text-transform: uppercase;
    white-space: nowrap;
  }
  .card--front .brand { top: 56px; font-size: 30px; }
  .card--back  .brand { top: 120px; font-size: 34px; }

  .details {
    position: absolute;
    top: 146px;
    left: 0; right: 0;
    display: flex;
    justify-content: center;
    white-space: nowrap;
  }
  .person {
    text-align: right;
    padding-right: 16px;
    border-right: 1px solid var(--divider);
    color: var(--text-light);
    font-size: 15px;
    line-height: 19px;
  }
  .person__name {
    color: var(--teal);
    font-weight: 600;
    font-size: 21px;
    line-height: 26px;
  }
  .person__title { margin-bottom: 14px; }

  .contact-list {
    list-style: none;
    padding-left: 14px;
    color: var(--text-light);
    font-size: 14.5px;
  }
  .contact-list li {
    display: flex;
    align-items: center;
    height: 24px;
  }
  .contact-icon {
    width: 15px;
    height: 15px;
    margin-right: 9px;
    flex: none;
  }
</style>
</head>
<body>
<main class="card-set">
  <section class="card card--front" aria-label="Card front">
    <div class="brand">Brisley Homes</div>
    <div class="details">
      <div class="person">
        <div class="person__name">Harold P. Brisley Jr.</div>
        <div class="person__title">Real Estate Broker</div>
        <div>BRE # 07390418</div>
        <div>Santa Clara County, CA</div>
      </div>
      <ul class="contact-list">
        <li>
          <svg class="contact-icon" viewBox="0 0 16 16" aria-hidden="true"><rect width="16" height="16" rx="2" fill="var(--teal)"/><path d="M4 6.5c0-1.5 2-2.5 4-2.5s4 1 4 2.5v.5h-2.2v-1H6.2v1H4z M4.5 8h7l.5 4H4z" fill="#fff"/></svg>
          (408) 555-0172
        </li>
        <li>
          <svg class="contact-icon" viewBox="0 0 16 16" aria-hidden="true"><rect width="16" height="16" rx="2" fill="var(--teal)"/><rect x="5" y="3" width="6" height="10" rx="1" fill="#fff"/><rect x="6" y="4.5" width="4" height="6" fill="var(--teal)"/></svg>
          (408) 555-0193
        </li>
        <li>
          <svg class="contact-icon" viewBox="0 0 16 16" aria-hidden="true"><rect width="16" height="16" rx="2" fill="var(--teal)"/><rect x="3.5" y="5" width="9" height="6.5" fill="#fff"/><path d="M3.5 5l4.5 3.6L12.5 5" fill="none" stroke="var(--teal)" stroke-width="1"/></svg>
          Hal@HaroldBrisley.example
        </li>
        <li>
          <svg class="contact-icon" viewBox="0 0 16 16" aria-hidden="true"><rect width="16" height="16" rx="2" fill="var(--teal)"/><path d="M6.5 9.5l3-3M7 5.5l1-1a2 2 0 0 1 3 3l-1 1M9 10.5l-1 1a2 2 0 0 1-3-3l1-1" fill="none" stroke="#fff" stroke-width="1.3" stroke-linecap="round"/></svg>
          www.HaroldBrisley.example
        </li>
      </ul>
    </div>
  </section>

  <section class="card card--back" aria-label="Card back">
    <div class="brand">Brisley Homes</div>
  </section>
</main>
</body>
</html>
```